Marisol Specialty Coffee needs a Packaging design

We need packaging design for coffee that suits our brand identity, that is the best quality in Mexico.
We only sell mexican coffee with Q scores above 80
We are evaluating 3 types of packaging: Bag, Box and Cillinder can
The specific package format will be decided based on the designs that we get.
Updates

Target Market(s)

Coffee experts and enthusiast.
People that relate the Coffee consumption and experience with wine tasting and Bon Vivant way

Requirements
Should not have
• Photos any mexican cliché

```html
<!DOCTYPE html>
<html lang="en">
<head>
<meta charset="utf-8">
<title>Marisol Specialty Coffee – Packaging</title>
<link href="https://fonts.googleapis.com/css2?family=Cormorant+Garamond:wght@500&family=Pinyon+Script&family=Arimo:wght@700&display=swap" rel="stylesheet">
<style>
  :root {
    --paper: #ffffff;
    --frame: #1a1a1a;
    --ink: #000000;
    --pack-black: #0b0a0a;
    --pack-brown: #16120f;
    --gold: #e3cf1f;
    --gold-deep: #c4ad07;
  }
  * { margin: 0; padding: 0; box-sizing: border-box; }
  html, body { width: 1086px; height: 1200px; overflow: hidden; background: var(--paper); }
  .sheet {
    position: relative;
    width: 1086px; height: 1200px;
    border: 2px solid var(--frame);
    background: var(--paper);
  }
  .panel { position: absolute; overflow: hidden; }
  .panel--front {
    left: 89px; top: 108px; width: 436px; height: 829px;
    background: linear-gradient(to bottom, var(--pack-black) 0 60%, var(--pack-brown) 60% 100%);
  }
  .panel--back {
    left: 564px; top: 100px; width: 438px; height: 834px;
    background: linear-gradient(to right, var(--pack-brown), var(--pack-black) 30%);
  }
  .brand {
    position: absolute; left: 0; right: 0; top: 140px;
    display: flex; flex-direction: column; align-items: center;
    color: var(--gold);
    font-family: "Cormorant Garamond", serif; font-weight: 500;
  }
  .brand__row { display: flex; align-items: center; gap: 16px; }
  .brand__mark { width: 22px; height: 22px; border-radius: 50%; background: var(--gold); }
  .brand__name { font-size: 62px; line-height: 1; letter-spacing: 1px; }
  .brand__tagline { font-size: 28px; margin-top: 8px; margin-left: 90px; letter-spacing: .5px; }
  .leaves {
    position: absolute; left: 0; right: 0; top: 355px; height: 160px;
    background: radial-gradient(ellipse at 50% 55%, rgba(227,207,31,.35), rgba(227,207,31,.08) 65%, transparent 85%);
  }
  .product-word {
    position: absolute; left: 0; right: 0; top: 560px;
    text-align: center; color: var(--gold);
    font-family: "Pinyon Script", cursive; font-size: 130px; line-height: 1.2;
  }
  .cone-art {
    position: absolute; left: 0; top: 0; width: 206px; height: 622px;
    background: linear-gradient(160deg, rgba(227,207,31,.55), rgba(196,173,7,.2) 55%, transparent 90%);
  }
  .band {
    position: absolute; left: 0; right: 0; bottom: 0; height: 48px;
    background: var(--gold-deep);
  }
  .label {
    position: absolute; top: 995px;
    font-family: "Arimo", Arial, sans-serif; font-weight: 700;
    font-size: 92px; color: var(--ink); transform: translateX(-50%);
  }
  .label--front { left: 311px; }
  .label--back { left: 796px; }
</style>
</head>
<body>
<main class="sheet">
  <section class="panel panel--front">
    <div class="brand">
      <div class="brand__row">
        <span class="brand__mark"></span>
        <span class="brand__name">Marisol</span>
      </div>
      <span class="brand__tagline">Specialty Coffee</span>
    </div>
    <div class="leaves" role="img" aria-label="Row of gold outline coffee leaves with fine veins"></div>
    <div class="product-word">Coffee</div>
  </section>

  <section class="panel panel--back">
    <div class="cone-art" role="img" aria-label="Shiny gold cone tapering down from a black ball at the top edge"></div>
    <div class="band"></div>
  </section>

  <span class="label label--front">Front</span>
  <span class="label label--back">Back</span>
</main>
</body>
</html>
```